NutriKeen children complimentary food package design

We need to design a bilingual (Arabic & English) baby complimentary powder food label, that is suitable for children from 1 to 10 years old. The primary purpose of this product is support healthy growth in general with special emphasis when the child is picky eater.
We want a design that is elegant, professional and western Looking. It will be printed onto a 400 grams can. The brand is called NutriKeen. The brand name is composed of two parts: "Nutri" which means advance and "Keen" which means ensured. The design should reflect this concept.
Be as creative as possible and we want the brands to have an classy, premium, elegant and professional feel, look and layout. Below are some requirements:
• Color theme: The general color is red keeping in mind that this product will be presented in different flavours: Vanilla, Chocolate and others.
• Unique ingredients/characteristics have to be mentioned on the front panel. Creative ideas are welcome and I am attaching illustrations from competitive products. The ingredients/characteristics are:
o DHA/AA
o 30 Vitamins & Minerals
o GMO free
• Although the brand name has a shield character, but we are looking to have a special character/emblem on the label that will be registered as a trademark. Creative ideas are welcome. Product images from other companies are attached as a reference. We are not limited to animal characters.
• The current organization of English and Arabic brand name is horizontal however this can be changes according to the designer discretion (e.g vertical).
Usually the label of infant formula can is divided into three parts: Left panel, Front panel and right Panel. Arabic text will be added later, just put a place holder and we will add it locally. We have no limitation for the number of colors. Usually the label has 4 process colors (CMYK) plus a number of spot colors and it is fine to use gold or silver color if deemed necessary for the label.
Updates
Target Market(s)
Children 1 - 10 years of age
Industry/Entity Type
Nutrition

```html
<!DOCTYPE html>
<html lang="en">
<head>
<meta charset="utf-8">
<title>NutriKeen – Vanilla Flavour Label</title>
<link rel="stylesheet" href="https://fonts.googleapis.com/css2?family=Rubik:wght@500;600;700&display=swap">
<style>
  :root {
    --page: #ffffff;
    --label-red: #d9493c;
    --label-red-light: #f08a78;
    --label-coral: #f3766a;
    --band-white: #f1f1f1;
    --band-cream: #f8f3dc;
    --brand-berry: #b8386a;
    --badge-fill: #e67f74;
    --badge-text: #6a1d7a;
    --tiger-yellow: #f0d524;
    --tiger-brown: #6b4420;
    --hand-yellow: #f3b12d;
    --hand-orange: #e98524;
    --foot-rose: #c95a63;
    --text-white: #ffffff;
  }
  * { margin: 0; padding: 0; box-sizing: border-box; }
  html, body {
    width: 1200px; height: 1080px; overflow: hidden;
    background: var(--page);
    font-family: "Rubik", sans-serif;
  }
  .label {
    position: absolute; left: 150px; top: 25px;
    width: 900px; height: 1030px; overflow: hidden;
    background:
      linear-gradient(100deg, var(--label-red-light) 0%, var(--label-red) 30%, var(--label-red) 70%, var(--label-coral) 100%);
  }
  .label-band { position: absolute; left: 0; top: 0; width: 900px; height: 520px; }
  .brand-name {
    position: absolute; left: 110px; top: 200px;
    font-weight: 700; font-size: 124px; line-height: 1;
    color: var(--brand-berry); letter-spacing: -1px; white-space: nowrap;
    transform: rotate(-8deg); transform-origin: left center;
  }
  .mascot {
    position: absolute; left: 575px; top: 300px;
    width: 210px; height: 300px; border-radius: 48% 48% 46% 46%;
    background: var(--tiger-yellow);
    border: 10px solid var(--tiger-brown);
    transform: rotate(10deg);
  }
  .mascot-call {
    position: absolute; left: 795px; top: 480px;
    color: var(--text-white); font-weight: 600; font-size: 28px; white-space: nowrap;
    transform: rotate(22deg); transform-origin: left top;
  }
  .handprints {
    position: absolute; left: 90px; top: 510px;
    width: 225px; height: 180px; border-radius: 40%;
    background: linear-gradient(90deg, var(--hand-yellow), var(--hand-orange));
    opacity: .85;
  }
  .footprints {
    position: absolute; left: 745px; top: 695px;
    width: 130px; height: 270px; border-radius: 45%;
    background: linear-gradient(180deg, var(--foot-rose), #b84b57);
    opacity: .75;
  }
  .claims { position: absolute; left: 0; top: 0; width: 900px; height: 1030px; }
  .claim {
    position: absolute; width: 96px; height: 124px;
    display: flex; align-items: center; justify-content: center; text-align: center;
    color: var(--badge-text); font-weight: 600; font-size: 20px; line-height: 1.4;
  }
  .claim svg { position: absolute; inset: 0; z-index: 0; }
  .claim span { position: relative; z-index: 1; white-space: nowrap; }
  .claim--dha { left: 242px; top: 743px; }
  .claim--vitamins { left: 410px; top: 743px; width: 160px; }
  .claim--gmo { left: 597px; top: 743px; }
  .flavour, .net-weight {
    position: absolute; left: 0; width: 900px; text-align: center;
    color: var(--text-white); font-weight: 600;
  }
  .flavour { top: 900px; font-size: 29px; }
  .net-weight { top: 977px; font-size: 29px; }
</style>
</head>
<body>
  <main class="label">
    <svg class="label-band" viewBox="0 0 900 520" aria-hidden="true">
      <path d="M0 0 H900 V180 C860 230 820 250 770 300 C700 360 640 380 570 360 C470 330 380 410 300 450 C200 500 80 470 0 400 Z" fill="var(--band-white)"/>
      <path d="M0 120 C60 200 40 320 0 400 Z" fill="var(--band-cream)"/>
      <path d="M120 0 C250 60 420 40 600 0 Z" fill="#e46a55" opacity=".55"/>
    </svg>

    <h1 class="brand-name">NutriKeen</h1>

    <div class="mascot" role="img" aria-label="Smiling yellow tiger cub character"></div>
    <p class="mascot-call">RAWRH</p>

    <div class="handprints" role="img" aria-label="Two painted child handprints in yellow and orange"></div>
    <div class="footprints" role="img" aria-label="Two baby footprints in soft rose"></div>

    <div class="claims">
      <div class="claim claim--dha">
        <svg viewBox="0 0 96 124" aria-hidden="true"><polygon points="48,0 72,14 96,32 96,92 72,110 48,124 24,110 0,92 0,32 24,14" fill="var(--badge-fill)"/></svg>
        <span>DHA/AA</span>
      </div>
      <div class="claim claim--vitamins">
        <svg viewBox="0 0 160 124" aria-hidden="true"><polygon points="80,0 112,14 140,32 140,92 112,110 80,124 48,110 20,92 20,32 48,14" fill="var(--badge-fill)"/></svg>
        <span>+30 vitmanis<br>&amp; minerals</span>
      </div>
      <div class="claim claim--gmo">
        <svg viewBox="0 0 96 124" aria-hidden="true"><polygon points="48,0 72,14 96,32 96,92 72,110 48,124 24,110 0,92 0,32 24,14" fill="var(--badge-fill)"/></svg>
        <span>GMO<br>free</span>
      </div>
    </div>

    <p class="flavour">Vanilla Flavour</p>
    <p class="net-weight">Net. Wt. 900g Powder</p>
  </main>
</body>
</html>
```